Website for a dog poop removal service.

The Pebble Crew specializes in professional and hassle-free pet waste removal services, ensuring your yard stays clean, fresh, and safe for your family and pets. We take care of the dirty work, so you don’t have to, offering reliable, scheduled cleanups tailored to your needs. Let us help you reclaim your time and enjoy a spotless, stress-free outdoor space!
We will need the winning website to be transferred to our domain located at Servalyne. We would like to have the following web pages.
Home
About
Services
Contact Us
Client Portal
FAQ
Blog
Free Quote
The Free Quote webpage and client portal will need to be integrated with the following our account on the following website: tidyroutex.com

```html
<!DOCTYPE html>
<html lang="en">
<head>
<meta charset="utf-8">
<title>The Pebble Crew — Website Home Page</title>
<link rel="stylesheet" href="https://fonts.googleapis.com/css2?family=Baloo+2:wght@500;600;700&family=Roboto:wght@400;500;700&display=swap">
<style>
:root{
  --green:#6bb23f;
  --green-dark:#4f9a2a;
  --tan:#c09b7c;
  --tan-dark:#a9836a;
  --cream:#f7f3f0;
  --ink:#1e1e1c;
  --grey:#6e6e6e;
  --board:#6f6f6f;
  --white:#ffffff;
}
*{box-sizing:border-box;margin:0;padding:0}
html,body{width:1200px;height:2668px;overflow:hidden;background:var(--board)}
body{position:relative;font-family:"Roboto",Arial,sans-serif;color:var(--ink)}
.page{position:absolute;top:83px;width:405px;background:var(--white);overflow:hidden}
.page--a{left:139px}
.page--b{left:599px}
section,header,footer{position:relative;width:405px;overflow:hidden}
.abs{position:absolute}
.h-display{font-family:"Baloo 2",Arial,sans-serif;font-weight:600;line-height:1.05}
.btn{position:absolute;display:flex;align-items:center;justify-content:center;font:700 5.2px/1 "Roboto",Arial,sans-serif;text-transform:uppercase;color:var(--white);border-radius:3px;letter-spacing:.2px}
.btn--green{background:var(--green)}
.btn--dark{background:var(--ink)}
.btn--tan{background:var(--tan);border:1px solid #e8d6c6}
.btn--outline{background:var(--green);border:1px solid #bfe0a8}
.photo{position:absolute}
.body-copy{font-size:4.4px;line-height:1.45;color:#3c3c3c}

/* top bar + header A */
.topbar{height:17px;background:var(--green);color:var(--white);font:700 5px/17px "Roboto",Arial,sans-serif}
.topbar__promo{position:absolute;left:135px}
.topbar__follow{position:absolute;right:26px;font-size:4px}
.social{display:inline-flex;gap:2px;vertical-align:middle;margin-left:3px}
.social i{display:inline-block;width:5px;height:5px;border:0.8px solid currentColor;border-radius:50%}
.header{background:var(--white)}
.page--a .header{height:46px}
.brand{position:absolute;display:flex;align-items:center;gap:4px;font:700 9px/1 "Baloo 2",Arial,sans-serif;color:var(--ink);white-space:nowrap}
.brand__mark{width:24px;height:24px;border-radius:50%;background:var(--green)}
.phone-pill{position:absolute;left:236px;top:8px;height:12px;padding:0 6px;border-radius:6px;background:var(--cream);font:700 5px/12px "Roboto",Arial,sans-serif;display:flex;align-items:center;gap:3px}
.nav{position:absolute;display:flex;gap:11px;font:700 4.6px/1 "Roboto",Arial,sans-serif;text-transform:uppercase}
.nav .is-active{color:var(--green)}
.page--b .header{height:50px;border-top:2px solid var(--tan)}
.follow{position:absolute;font:700 4px/1 "Roboto",Arial,sans-serif}

/* hero */
.hero{height:201px}
.page--b .hero{height:200px}
.hero__photo{left:0;top:0;width:405px;height:190px;background:linear-gradient(160deg,#8fbf56 0%,#b9d98a 35%,#6c9d3a 70%,#4f8a2b 100%)}
.hero__badge{position:absolute;left:200px;top:14px;width:186px;height:186px;border-radius:50%;background:var(--tan);border:4px solid rgba(255,255,255,.25);box-shadow:inset 0 0 0 3px var(--tan-dark)}
.hero__badge-inner{position:absolute;left:22px;top:30px;width:142px;text-align:center;color:var(--white)}
.hero__title{font-size:13.5px}
.hero__text{font-size:5px;line-height:1.3;margin-top:3px}
.hero__wave{position:absolute;left:0;bottom:0}

/* promise */
.promise{height:264px;background:var(--cream)}
.section-title{position:absolute;left:0;width:405px;text-align:center;font-size:13px;color:var(--ink)}
.mascot{position:absolute;background:radial-gradient(circle at 50% 40%,#ffffff 0,#f1ece6 45%,#7fbf52 46%,#6bb23f 100%);border-radius:45% 45% 20% 20%}
.feature{position:absolute;width:96px}
.feature--right{text-align:right}
.feature__icon{position:absolute;top:2px;width:20px;height:20px}
.feature__title{font:700 5px/1.15 "Roboto",Arial,sans-serif;margin-bottom:7px}
.feature__text{font-size:4.2px;line-height:1.35;color:#3c3c3c}
.curve{position:absolute;left:0}

/* about */
.about{height:248px}
.about__title{position:absolute;left:43px;top:46px;font-size:13px}
.about__copy{position:absolute;left:43px;top:84px;width:138px}
.about__copy p+p{margin-top:5px}
.about__photo{position:absolute;left:202px;top:36px;width:162px;height:162px;border-radius:50%;background:linear-gradient(170deg,#3f6d2d 0%,#5f8d3c 45%,#d9dcdc 55%,#b7b9b8 100%);border:1.5px solid #9ac47a}

/* how it works */
.how{height:235px;background:linear-gradient(#f8f5f2,#ffffff)}
.how__title{top:52px}
.step{position:absolute;top:92px;width:96px;text-align:center}
.step__icon{width:34px;height:34px;margin:0 auto;border-radius:6px;background:#e9f3df;border:1.5px solid var(--ink)}
.step__base{width:48px;height:5px;margin:2px auto 0;border-radius:50%;background:var(--green)}
.step__title{margin-top:26px;font:500 5.6px/1 "Roboto",Arial,sans-serif;color:var(--green)}
.step__text{margin-top:5px;font-size:4.3px;line-height:1.35;color:#3c3c3c}

/* call to action */
.cta{height:190px;background:var(--green)}
.cta__title{position:absolute;left:198px;top:32px;font-size:19px;color:var(--white)}
.cta__text{position:absolute;left:198px;top:83px;width:150px;font-size:8.6px;line-height:1.25;color:var(--white)}
.cta__shadow{position:absolute;left:42px;top:150px;width:120px;height:14px;border-radius:50%;background:var(--tan)}

/* services */
.services{height:255px;background:linear-gradient(120deg,#c6a283 0%,#b8926f 60%,#c7a587 100%)}
.services__title{position:absolute;left:43px;top:22px;font-size:13px;color:var(--white)}
.services__rule{position:absolute;left:75px;top:58px;width:18px;height:1.5px;background:var(--white)}
.service-card{position:absolute;top:74px;width:80px;height:122px;background:var(--white);border-radius:4px;text-align:center;padding:12px 6px 0}
.service-card__icon{width:24px;height:24px;margin:0 auto}
.service-card__title{margin-top:6px;font:700 5.2px/1.15 "Roboto",Arial,sans-serif}
.service-card__text{margin-top:6px;font-size:4.1px;line-height:1.35;color:#3c3c3c}

/* testimonials */
.testimonials{height:230px}
.testimonials__title{top:46px}
.quote-card{position:absolute;top:82px;width:152px;height:106px;border-radius:10px;background:var(--white);box-shadow:0 2px 6px rgba(0,0,0,.14);text-align:center;padding:14px 18px 0}
.quote-card__stars{color:var(--green);font-size:8px;letter-spacing:2px;line-height:1}
.quote-card__text{margin-top:7px;font-size:4.6px;line-height:1.4;font-style:italic;color:#3c3c3c}
.quote-card__name{margin-top:7px;font:700 4.6px/1 "Roboto",Arial,sans-serif;color:var(--tan)}
.arrow{position:absolute;top:126px}

/* gallery */
.gallery{height:214px}
.gallery__title{top:22px}
.gallery__photo{position:absolute;top:50px;height:146px;border-radius:12px}

/* faq */
.faq{height:346px;background:var(--cream)}
.faq__title{top:58px}
.faq__list{position:absolute;left:80px;top:106px;width:246px;list-style:none}
.faq__item{height:19.7px;display:flex;align-items:center;justify-content:space-between;border-bottom:0.7px solid #d8d2cc;font:500 6.2px/1 "Roboto",Arial,sans-serif}
.faq__item span{font-size:7px}

/* fence + footer */
.fence{height:83px;background:linear-gradient(#ffffff 0%,#f5f1ea 35%,#e9dcba 55%,#8cc260 85%,var(--green) 100%)}
.footer{height:152px;background:var(--green);color:var(--white)}
.footer__col{position:absolute;top:12px;padding-left:14px;border-left:1px solid rgba(255,255,255,.6)}
.footer__heading{font-size:9px;margin-bottom:8px}
.footer__links{display:grid;grid-template-columns:52px 52px;row-gap:4px;font-size:4.2px;list-style:none}
.footer__contact{font-size:4.2px;line-height:1.3;list-style:none}
.footer__contact li{display:flex;gap:5px;margin-bottom:6px}
.footer__copy{position:absolute;left:135px;font-size:4.2px}
.footer__social{position:absolute;display:flex;gap:3px}
.footer__social i{width:11px;height:11px;border-radius:50%;background:var(--white)}
</style>
</head>
<body>

<!-- ================= Variant A ================= -->
<main class="page page--a" style="height:2481px">
  <div class="topbar">
    <span class="topbar__promo">FREE INITIAL CLEANUP WITH REGULAR SERVICE!</span>
    <span class="topbar__follow">FOLLOW US: <span class="social"><i></i><i></i><i></i></span></span>
  </div>
  <header class="header">
    <div class="brand" style="left:20px;top:10px"><span class="brand__mark"></span>The Pebble Crew</div>
    <div class="phone-pill">
      <svg width="6" height="6" viewBox="0 0 24 24"><path d="M6 2l4 4-2 3a12 12 0 0 0 7 7l3-2 4 4-3 4C10 22 2 14 2 5z" fill="#6bb23f"/></svg>
      PHONE: (555) 014-7720
    </div>
    <div class="btn btn--green" style="left:330px;top:6px;width:53px;height:16px;font-size:5.4px">Free Quote</div>
    <nav class="nav" style="left:152px;top:34px">
      <span class="is-active">Home</span><span>About</span><span>Services</span><span>Contact Us</span><span>Client Portal</span><span>FAQ</span><span>Blog</span>
    </nav>
  </header>

  <section class="hero">
    <div class="photo hero__photo" role="img" aria-label="Photo of a family playing with a white dog on a green lawn"></div>
    <div class="hero__badge">
      <div class="hero__badge-inner">
        <div class="h-display hero__title">Keeping Your<br>Yard Clean, Fresh<br>and Hassle-Free!"</div>
        <p class="hero__text">Professional pet waste removal services<br>tailored to your needs.</p>
      </div>
      <div class="btn btn--outline" style="left:24px;top:112px;width:134px;height:15px">Get a Free Quote Today!</div>
      <div class="btn btn--dark" style="left:24px;top:132px;width:134px;height:15px">Schedule Your First Cleanup Now!</div>
    </div>
    <svg class="hero__wave" width="405" height="40" viewBox="0 0 405 40">
      <path d="M0 20 C90 0 190 38 290 22 S380 6 405 14 V40 H0Z" fill="#f7f3f0"/>
      <path d="M0 22 C90 2 190 40 290 24 S380 8 405 16" stroke="#6bb23f" stroke-width="3" fill="none"/>
      <path d="M0 28 C100 12 200 40 300 30 S385 16 405 20" stroke="#ffffff" stroke-width="2" fill="none"/>
    </svg>
  </section>

  <section class="promise">
    <h2 class="h-display section-title" style="top:34px">The Pebble Crew<br>Customer Promise!</h2>
    <div class="mascot" role="img" aria-label="Illustration of the cartoon dog mascot holding a scooper" style="left:133px;top:70px;width:130px;height:150px"></div>
    <div class="feature" style="left:43px;top:95px">
      <svg class="feature__icon" style="left:0" viewBox="0 0 24 24"><rect x="3" y="8" width="14" height="12" rx="2" fill="#dcefcf" stroke="#1e1e1c"/><path d="M7 8V5h6v3" stroke="#1e1e1c" fill="none"/></svg>
      <div style="padding-left:30px"><div class="feature__title">Reliable,<br>scheduled cleanups</div><p class="feature__text">Regular visits on a set day so your lawn stays tidy every week.</p></div>
    </div>
    <div class="feature feature--right" style="left:270px;top:95px">
      <svg class="feature__icon" style="right:0" viewBox="0 0 24 24"><circle cx="16" cy="8" r="6" fill="#dcefcf" stroke="#1e1e1c"/><path d="M2 18h12" stroke="#1e1e1c"/></svg>
      <div style="padding-right:30px"><div class="feature__title">Affordable and<br>hassle-free</div><p class="feature__text">Clear, fair pricing with no contracts and nothing to worry about.</p></div>
    </div>
    <div class="feature" style="left:43px;top:168px">
      <svg class="feature__icon" style="left:0" viewBox="0 0 24 24"><path d="M12 3l8 4v6c0 4-4 7-8 8-4-1-8-4-8-8V7z" fill="#dcefcf" stroke="#1e1e1c"/></svg>
      <div style="padding-left:30px"><div class="feature__title">Safe for pets<br>and family</div><p class="feature__text">Careful methods that keep kids and pets safe on the grass.</p></div>
    </div>
    <div class="feature feature--right" style="left:270px;top:168px">
      <svg class="feature__icon" style="right:0" viewBox="0 0 24 24"><path d="M12 20V10M12 10c0-4 4-6 8-6 0 4-4 6-8 6zM12 12c0-3-3-5-7-5 0 3 3 5 7 5z" fill="#dcefcf" stroke="#1e1e1c"/></svg>
      <div style="padding-right:30px"><div class="feature__title">Environmentally<br>responsible disposal</div><p class="feature__text">Waste is bagged and disposed of the clean, green way.</p></div>
    </div>
    <svg class="curve" style="bottom:0" width="405" height="40" viewBox="0 0 405 40"><path d="M0 20 C130 45 260 40 405 0 V40 H0Z" fill="#ffffff"/></svg>
  </section>

  <section class="about">
    <h2 class="h-display about__title">About<br>The Pebble Crew</h2>
    <div class="about__copy body-copy">
      <p>We're passionate about making life easier for pet owners. Our professional team is dedicated to ensuring your yard stays clean, healthy, and stress-free. With flexible scheduling, affordable rates, and top-notch customer service, we make pet ownership even more enjoyable.</p>
      <p>The Pebble Crew specializes in professional and hassle-free pet waste removal services, ensuring your yard stays clean, fresh, and safe for your family and pets. We take care of the dirty work, so you don't have to, offering reliable, scheduled cleanups tailored to your needs. Let us help you reclaim your time and enjoy a spotless, stress-free outdoor space!</p>
    </div>
    <div class="btn btn--green" style="left:43px;top:198px;width:55px;height:16px;border-radius:5px">Read More</div>
    <div class="about__photo" role="img" aria-label="Photo of the company's white pickup truck parked in front of green hedges"></div>
    <svg class="curve" style="bottom:0" width="405" height="30" viewBox="0 0 405 30"><path d="M0 18 C120 4 250 30 405 12" stroke="#c09b7c" stroke-width=".7" fill="none"/><path d="M0 22 C140 10 260 34 405 16" stroke="#6bb23f" stroke-width=".7" fill="none"/></svg>
  </section>

  <section class="how">
    <h2 class="h-display section-title how__title">How The Pebble Crew Works?</h2>
    <div class="step" style="left:40px"><div class="step__icon" role="img" aria-label="Calendar icon illustration"></div><div class="step__base"></div><div class="step__title">Book Appointment</div><p class="step__text">Pick a time that suits you and we will confirm your first visit quickly.</p></div>
    <div class="step" style="left:155px"><div class="step__icon" role="img" aria-label="Mascot dog illustration" style="border-radius:50%"></div><div class="step__base"></div><div class="step__title">We Take Care Of Business</div><p class="step__text">Our crew arrives on schedule and clears every corner of the yard.</p></div>
    <div class="step" style="left:269px"><div class="step__icon" role="img" aria-label="Clean yard with fence and tree illustration"></div><div class="step__base"></div><div class="step__title">Enjoy A Clean Yard</div><p class="step__text">Relax outdoors with your family in a fresh and spotless space.</p></div>
  </section>

  <section class="cta">
    <div class="cta__shadow"></div>
    <div class="mascot" role="img" aria-label="Illustration of the cartoon dog mascot with a scooper" style="left:48px;top:24px;width:108px;height:134px"></div>
    <h2 class="h-display cta__title">Let's Keep Your<br>Yard Clean!</h2>
    <p class="cta__text">Ready to schedule your cleanup or have questions? We'd love to hear from you.</p>
    <div class="btn btn--tan" style="left:198px;top:133px;width:100px;height:15px">Get a Free Quote Today!</div>
  </section>

  <section class="services" role="img" aria-label="Soft background photo of a person relaxing outdoors">
    <h2 class="h-display services__title">Our Services<br>Tailored to Your Needs</h2>
    <div class="services__rule"></div>
    <article class="service-card" style="left:35px"><svg class="service-card__icon" viewBox="0 0 24 24"><path d="M8 2v12M5 14h6l2 8H3z" fill="#dcefcf" stroke="#1e1e1c"/></svg><div class="service-card__title">Weekly<br>Cleanups</div><p class="service-card__text">Keep your yard spotless with our regular cleanup services. Ideal for maintaining a fresh and clean outdoor space.</p></article>
    <article class="service-card" style="left:122px"><svg class="service-card__icon" viewBox="0 0 24 24"><circle cx="9" cy="9" r="7" fill="#dcefcf" stroke="#1e1e1c"/><path d="M9 5v4l3 2" stroke="#1e1e1c" fill="none"/></svg><div class="service-card__title">One-Time<br>Cleanups</div><p class="service-card__text">Need help before a special event or after a busy week? We've got you covered with our one-time cleanup service.</p></article>
    <article class="service-card" style="left:209px"><svg class="service-card__icon" viewBox="0 0 24 24"><rect x="3" y="5" width="16" height="15" rx="2" fill="#dcefcf" stroke="#1e1e1c"/><path d="M3 9h16" stroke="#1e1e1c"/></svg><div class="service-card__title">Custom<br>Schedules</div><p class="service-card__text">Choose a schedule that fits your lifestyle. We offer flexible options to ensure your yard stays pristine.</p></article>
    <article class="service-card" style="left:296px"><svg class="service-card__icon" viewBox="0 0 24 24"><path d="M3 11l9-8 9 8v10H3z" fill="#dcefcf" stroke="#1e1e1c"/></svg><div class="service-card__title">Commercial<br>Services</div><p class="service-card__text">Perfect for parks, apartment complexes, and other dog-friendly spaces. Let us handle the mess while you focus on your property.</p></article>
    <div class="btn btn--green" style="left:152px;top:214px;width:100px;height:15px">Get a Free Quote Today!</div>
  </section>

  <section class="testimonials">
    <h2 class="h-display section-title testimonials__title">Client Testimonials</h2>
    <svg class="arrow" style="left:22px" width="10" height="16" viewBox="0 0 10 16"><path d="M8 1L2 8l6 7" stroke="#1e1e1c" stroke-width="1.4" fill="none"/></svg>
    <article class="quote-card" style="left:45px"><div class="quote-card__stars">★★★★★</div><p class="quote-card__text">Friendly crew, always on time, and our lawn has never looked better. The kids can finally play outside without watching every step. We recommend them to every dog owner.</p><div class="quote-card__name">MARLA T.</div></article>
    <article class="quote-card" style="left:206px"><div class="quote-card__stars">★★★★★</div><p class="quote-card__text">Friendly crew, always on time, and our lawn has never looked better. The kids can finally play outside without watching every step. We recommend them to every dog owner.</p><div class="quote-card__name">MARLA T.</div></article>
    <svg class="arrow" style="left:371px" width="10" height="16" viewBox="0 0 10 16"><path d="M2 1l6 7-6 7" stroke="#1e1e1c" stroke-width="1.4" fill="none"/></svg>
  </section>

  <section class="gallery">
    <h2 class="h-display section-title gallery__title">Enjoy a relaxing afternoon</h2>
    <div class="gallery__photo" role="img" aria-label="Photo of a couple with a dog outside their home" style="left:-10px;width:90px;background:linear-gradient(#b9c3c7,#6f8f52)"></div>
    <div class="gallery__photo" role="img" aria-label="Photo of a family sitting on the grass with a white dog" style="left:90px;width:225px;background:linear-gradient(#8fbf56,#5f9a36)"></div>
    <div class="gallery__photo" role="img" aria-label="Photo of a family with a dog in front of a house" style="left:325px;width:90px;background:linear-gradient(#c5c9c4,#7a9a58)"></div>
  </section>

  <section class="faq">
    <svg class="curve" style="top:0" width="405" height="50" viewBox="0 0 405 50"><path d="M0 0 H405 V18 C300 2 150 10 0 40Z" fill="#ffffff"/><path d="M0 40 C150 10 300 2 405 18" stroke="#6bb23f" stroke-width="4" fill="none"/></svg>
    <h2 class="h-display section-title faq__title">Frequently Asked<br>The Pebble Crew Questions!</h2>
    <ul class="faq__list">
      <li class="faq__item">What does your dog poop removal service include?<span>+</span></li>
      <li class="faq__item">Do you service all yard sizes?<span>+</span></li>
      <li class="faq__item">How often can I schedule your services?<span>+</span></li>
      <li class="faq__item">Are you environmentally friendly?<span>+</span></li>
      <li class="faq__item">What areas do you serve?<span>+</span></li>
      <li class="faq__item">Do I need to be home during the service?<span>+</span></li>
      <li class="faq__item">Can you clean up after multiple dogs?<span>+</span></li>
      <li class="faq__item">Do you work in bad weather?<span>+</span></li>
      <li class="faq__item">How much does your service cost?<span>+</span></li>
    </ul>
    <div class="btn btn--green" style="left:170px;top:304px;width:64px;height:17px;font-size:6px">View All</div>
  </section>

  <div class="fence" role="img" aria-label="Illustration of a picket fence with bushes and grass"></div>

  <footer class="footer">
    <div class="mascot" role="img" aria-label="Illustration of the cartoon dog mascot" style="left:40px;top:12px;width:82px;height:104px"></div>
    <div class="footer__col" style="left:135px">
      <div class="h-display footer__heading">Links</div>
      <ul class="footer__links"><li>Home</li><li>Blog</li><li>About</li><li>Free Quote</li><li>Services</li><li>Testimonials</li><li>Contact Us</li><li>Community</li><li>Client Portal</li><li>Privacy Policy</li><li>FAQ</li><li>Terms &amp; Conditions</li></ul>
    </div>
    <div class="footer__col" style="left:260px">
      <div class="h-display footer__heading">Contact</div>
      <ul class="footer__contact">
        <li><svg width="5" height="6" viewBox="0 0 10 12"><path d="M5 0a4 4 0 0 1 4 4c0 3-4 8-4 8S1 7 1 4a4 4 0 0 1 4-4z" fill="#fff"/></svg><span>418 Meadowlark Ln,<br>Fairview, ST 00000</span></li>
        <li><svg width="5" height="5" viewBox="0 0 10 10"><rect x="1" y="2" width="8" height="6" fill="#fff"/></svg><span>Phone:<br>(555) 014-7720</span></li>
        <li><svg width="5" height="5" viewBox="0 0 24 24"><path d="M6 2l4 4-2 3a12 12 0 0 0 7 7l3-2 4 4-3 4C10 22 2 14 2 5z" fill="#fff"/></svg><span>Email:<br>hello@pebblecrew.example</span></li>
      </ul>
    </div>
    <div class="footer__copy" style="top:134px">Copyright © 2025 The Pebble Crew. All Rights Are Reserved.</div>
    <div class="footer__social" style="left:318px;top:130px"><i></i><i></i><i></i></div>
  </footer>
</main>

<!-- ================= Variant B ================= -->
<main class="page page--b" style="height:2465px">
  <header class="header">
    <div class="brand" style="left:12px;top:10px"><span class="brand__mark"></span>The Pebble Crew</div>
    <div class="follow" style="left:182px;top:13px">FOLLOW US: <span class="social" style="color:var(--tan)"><i></i><i></i><i></i></span></div>
    <div class="btn btn--green" style="left:247px;top:6px;width:140px;height:15px;font-size:4.8px">Free Initial Cleanup With Regular Service!</div>
    <nav class="nav" style="left:104px;top:33px">
      <span class="is-active">Home</span><span>About</span><span>Services</span><span>Contact Us</span><span>Client Portal</span><span>FAQ</span><span>Blog</span>
    </nav>
    <div class="btn btn--tan" style="left:347px;top:29px;width:40px;height:12px;font-size:4.4px">Free Quote</div>
  </header>

  <section class="hero">
    <div class="photo hero__photo" role="img" aria-label="Photo of a family playing with a white dog on a green lawn"></div>
    <div class="hero__badge">
      <div class="hero__badge-inner">
        <div class="h-display hero__title">Keeping Your<br>Yard Clean, Fresh<br>and Hassle-Free!"</div>
        <p class="hero__text">Professional pet waste removal services<br>tailored to your needs.</p>
      </div>
      <div class="btn btn--outline" style="left:24px;top:112px;width:134px;height:15px">Get a Free Quote Today!</div>
      <div class="btn btn--dark" style="left:24px;top:132px;width:134px;height:15px">Schedule Your First Cleanup Now!</div>
    </div>
    <svg class="hero__wave" width="405" height="40" viewBox="0 0 405 40">
      <path d="M0 20 C90 0 190 38 290 22 S380 6 405 14 V40 H0Z" fill="#f7f3f0"/>
      <path d="M0 22 C90 2 190 40 290 24 S380 8 405 16" stroke="#6bb23f" stroke-width="3" fill="none"/>
      <path d="M0 28 C100 12 200 40 300 30 S385 16 405 20" stroke="#ffffff" stroke-width="2" fill="none"/>
    </svg>
  </section>

  <section class="promise">
    <h2 class="h-display section-title" style="top:34px">The Pebble Crew<br>Customer Promise!</h2>
    <div class="mascot" role="img" aria-label="Illustration of the cartoon dog mascot holding a scooper" style="left:133px;top:70px;width:130px;height:150px"></div>
    <div class="feature" style="left:43px;top:95px">
      <svg class="feature__icon" style="left:0" viewBox="0 0 24 24"><rect x="3" y="8" width="14" height="12" rx="2" fill="#dcefcf" stroke="#1e1e1c"/><path d="M7 8V5h6v3" stroke="#1e1e1c" fill="none"/></svg>
      <div style="padding-left:30px"><div class="feature__title">Reliable,<br>scheduled cleanups</div><p class="feature__text">Regular visits on a set day so your lawn stays tidy every week.</p></div>
    </div>
    <div class="feature feature--right" style="left:270px;top:95px">
      <svg class="feature__icon" style="right:0" viewBox="0 0 24 24"><circle cx="16" cy="8" r="6" fill="#dcefcf" stroke="#1e1e1c"/><path d="M2 18h12" stroke="#1e1e1c"/></svg>
      <div style="padding-right:30px"><div class="feature__title">Affordable and<br>hassle-free</div><p class="feature__text">Clear, fair pricing with no contracts and nothing to worry about.</p></div>
    </div>
    <div class="feature" style="left:43px;top:168px">
      <svg class="feature__icon" style="left:0" viewBox="0 0 24 24"><path d="M12 3l8 4v6c0 4-4 7-8 8-4-1-8-4-8-8V7z" fill="#dcefcf" stroke="#1e1e1c"/></svg>
      <div style="padding-left:30px"><div class="feature__title">Safe for pets<br>and family</div><p class="feature__text">Careful methods that keep kids and pets safe on the grass.</p></div>
    </div>
    <div class="feature feature--right" style="left:270px;top:168px">
      <svg class="feature__icon" style="right:0" viewBox="0 0 24 24"><path d="M12 20V10M12 10c0-4 4-6 8-6 0 4-4 6-8 6zM12 12c0-3-3-5-7-5 0 3 3 5 7 5z" fill="#dcefcf" stroke="#1e1e1c"/></svg>
      <div style="padding-right:30px"><div class="feature__title">Environmentally<br>responsible disposal</div><p class="feature__text">Waste is bagged and disposed of the clean, green way.</p></div>
    </div>
    <svg class="curve" style="bottom:0" width="405" height="40" viewBox="0 0 405 40"><path d="M0 20 C130 45 260 40 405 0 V40 H0Z" fill="#ffffff"/></svg>
  </section>

  <section class="about">
    <h2 class="h-display about__title">About<br>The Pebble Crew</h2>
    <div class="about__copy body-copy">
      <p>We're passionate about making life easier for pet owners. Our professional team is dedicated to ensuring your yard stays clean, healthy, and stress-free. With flexible scheduling, affordable rates, and top-notch customer service, we make pet ownership even more enjoyable.</p>
      <p>The Pebble Crew specializes in professional and hassle-free pet waste removal services, ensuring your yard stays clean, fresh, and safe for your family and pets. We take care of the dirty work, so you don't have to, offering reliable, scheduled cleanups tailored to your needs. Let us help you reclaim your time and enjoy a spotless, stress-free outdoor space!</p>
    </div>
    <div class="btn btn--green" style="left:43px;top:198px;width:55px;height:16px;border-radius:5px">Read More</div>
    <div class="about__photo" role="img" aria-label="Photo of the company's white pickup truck parked in front of green hedges"></div>
    <svg class="curve" style="bottom:0" width="405" height="30" viewBox="0 0 405 30"><path d="M0 18 C120 4 250 30 405 12" stroke="#c09b7c" stroke-width=".7" fill="none"/><path d="M0 22 C140 10 260 34 405 16" stroke="#6bb23f" stroke-width=".7" fill="none"/></svg>
  </section>

  <section class="how">
    <h2 class="h-display section-title how__title">How The Pebble Crew Works?</h2>
    <div class="step" style="left:40px"><div class="step__icon" role="img" aria-label="Calendar icon illustration"></div><div class="step__base"></div><div class="step__title">Book Appointment</div><p class="step__text">Pick a time that suits you and we will confirm your first visit quickly.</p></div>
    <div class="step" style="left:155px"><div class="step__icon" role="img" aria-label="Mascot dog illustration" style="border-radius:50%"></div><div class="step__base"></div><div class="step__title">We Take Care Of Business</div><p class="step__text">Our crew arrives on schedule and clears every corner of the yard.</p></div>
    <div class="step" style="left:269px"><div class="step__icon" role="img" aria-label="Clean yard with fence and tree illustration"></div><div class="step__base"></div><div class="step__title">Enjoy A Clean Yard</div><p class="step__text">Relax outdoors with your family in a fresh and spotless space.</p></div>
  </section>

  <section class="cta">
    <div class="cta__shadow"></div>
    <div class="mascot" role="img" aria-label="Illustration of the cartoon dog mascot with a scooper" style="left:48px;top:24px;width:108px;height:134px"></div>
    <h2 class="h-display cta__title">Let's Keep Your<br>Yard Clean!</h2>
    <p class="cta__text">Ready to schedule your cleanup or have questions? We'd love to hear from you.</p>
    <div class="btn btn--tan" style="left:198px;top:133px;width:100px;height:15px">Get a Free Quote Today!</div>
  </section>

  <section class="services" role="img" aria-label="Soft background photo of a person relaxing outdoors">
    <h2 class="h-display services__title">Our Services<br>Tailored to Your Needs</h2>
    <div class="services__rule"></div>
    <article class="service-card" style="left:35px"><svg class="service-card__icon" viewBox="0 0 24 24"><path d="M8 2v12M5 14h6l2 8H3z" fill="#dcefcf" stroke="#1e1e1c"/></svg><div class="service-card__title">Weekly<br>Cleanups</div><p class="service-card__text">Keep your yard spotless with our regular cleanup services. Ideal for maintaining a fresh and clean outdoor space.</p></article>
    <article class="service-card" style="left:122px"><svg class="service-card__icon" viewBox="0 0 24 24"><circle cx="9" cy="9" r="7" fill="#dcefcf" stroke="#1e1e1c"/><path d="M9 5v4l3 2" stroke="#1e1e1c" fill="none"/></svg><div class="service-card__title">One-Time<br>Cleanups</div><p class="service-card__text">Need help before a special event or after a busy week? We've got you covered with our one-time cleanup service.</p></article>
    <article class="service-card" style="left:209px"><svg class="service-card__icon" viewBox="0 0 24 24"><rect x="3" y="5" width="16" height="15" rx="2" fill="#dcefcf" stroke="#1e1e1c"/><path d="M3 9h16" stroke="#1e1e1c"/></svg><div class="service-card__title">Custom<br>Schedules</div><p class="service-card__text">Choose a schedule that fits your lifestyle. We offer flexible options to ensure your yard stays pristine.</p></article>
    <article class="service-card" style="left:296px"><svg class="service-card__icon" viewBox="0 0 24 24"><path d="M3 11l9-8 9 8v10H3z" fill="#dcefcf" stroke="#1e1e1c"/></svg><div class="service-card__title">Commercial<br>Services</div><p class="service-card__text">Perfect for parks, apartment complexes, and other dog-friendly spaces. Let us handle the mess while you focus on your property.</p></article>
    <div class="btn btn--green" style="left:152px;top:214px;width:100px;height:15px">Get a Free Quote Today!</div>
  </section>

  <section class="testimonials">
    <h2 class="h-display section-title testimonials__title">Client Testimonials</h2>
    <svg class="arrow" style="left:22px" width="10" height="16" viewBox="0 0 10 16"><path d="M8 1L2 8l6 7" stroke="#1e1e1c" stroke-width="1.4" fill="none"/></svg>
    <article class="quote-card" style="left:45px"><div class="quote-card__stars">★★★★★</div><p class="quote-card__text">Friendly crew, always on time, and our lawn has never looked better. The kids can finally play outside without watching every step. We recommend them to every dog owner.</p><div class="quote-card__name">MARLA T.</div></article>
    <article class="quote-card" style="left:206px"><div class="quote-card__stars">★★★★★</div><p class="quote-card__text">Friendly crew, always on time, and our lawn has never looked better. The kids can finally play outside without watching every step. We recommend them to every dog owner.</p><div class="quote-card__name">MARLA T.</div></article>
    <svg class="arrow" style="left:371px" width="10" height="16" viewBox="0 0 10 16"><path d="M2 1l6 7-6 7" stroke="#1e1e1c" stroke-width="1.4" fill="none"/></svg>
  </section>

  <section class="gallery">
    <h2 class="h-display section-title gallery__title">Enjoy a relaxing afternoon</h2>
    <div class="gallery__photo" role="img" aria-label="Photo of a couple with a dog outside their home" style="left:-10px;width:90px;background:linear-gradient(#b9c3c7,#6f8f52)"></div>
    <div class="gallery__photo" role="img" aria-label="Photo of a family sitting on the grass with a white dog" style="left:90px;width:225px;background:linear-gradient(#8fbf56,#5f9a36)"></div>
    <div class="gallery__photo" role="img" aria-label="Photo of a family with a dog in front of a house" style="left:325px;width:90px;background:linear-gradient(#c5c9c4,#7a9a58)"></div>
  </section>

  <section class="faq">
    <svg class="curve" style="top:0" width="405" height="50" viewBox="0 0 405 50"><path d="M0 0 H405 V18 C300 2 150 10 0 40Z" fill="#ffffff"/><path d="M0 40 C150 10 300 2 405 18" stroke="#6bb23f" stroke-width="4" fill="none"/></svg>
    <h2 class="h-display section-title faq__title">Frequently Asked<br>The Pebble Crew Questions!</h2>
    <ul class="faq__list">
      <li class="faq__item">What does your dog poop removal service include?<span>+</span></li>
      <li class="faq__item">Do you service all yard sizes?<span>+</span></li>
      <li class="faq__item">How often can I schedule your services?<span>+</span></li>
      <li class="faq__item">Are you environmentally friendly?<span>+</span></li>
      <li class="faq__item">What areas do you serve?<span>+</span></li>
      <li class="faq__item">Do I need to be home during the service?<span>+</span></li>
      <li class="faq__item">Can you clean up after multiple dogs?<span>+</span></li>
      <li class="faq__item">Do you work in bad weather?<span>+</span></li>
      <li class="faq__item">How much does your service cost?<span>+</span></li>
    </ul>
    <div class="btn btn--green" style="left:170px;top:304px;width:64px;height:17px;font-size:6px">View All</div>
  </section>

  <div class="fence" role="img" aria-label="Illustration of a picket fence with bushes and grass"></div>

  <footer class="footer" style="height:136px">
    <div class="mascot" role="img" aria-label="Illustration of the cartoon dog mascot" style="left:40px;top:12px;width:82px;height:100px"></div>
    <div class="footer__col" style="left:135px">
      <div class="h-display footer__heading">Links</div>
      <ul class="footer__links"><li>Home</li><li>Blog</li><li>About</li><li>Free Quote</li><li>Services</li><li>Testimonials</li><li>Contact Us</li><li>Community</li><li>Client Portal</li><li>Privacy Policy</li><li>FAQ</li><li>Terms &amp; Conditions</li></ul>
    </div>
    <div class="footer__col" style="left:260px">
      <div class="h-display footer__heading">Contact</div>
      <ul class="footer__contact">
        <li><svg width="5" height="6" viewBox="0 0 10 12"><path d="M5 0a4 4 0 0 1 4 4c0 3-4 8-4 8S1 7 1 4a4 4 0 0 1 4-4z" fill="#fff"/></svg><span>418 Meadowlark Ln,<br>Fairview, ST 00000</span></li>
        <li><svg width="5" height="5" viewBox="0 0 10 10"><rect x="1" y="2" width="8" height="6" fill="#fff"/></svg><span>Phone:<br>(555) 014-7720</span></li>
        <li><svg width="5" height="5" viewBox="0 0 24 24"><path d="M6 2l4 4-2 3a12 12 0 0 0 7 7l3-2 4 4-3 4C10 22 2 14 2 5z" fill="#fff"/></svg><span>Email:<br>hello@pebblecrew.example</span></li>
      </ul>
    </div>
    <div class="footer__copy" style="top:122px;left:135px">Copyright © 2025 The Pebble Crew. All Rights Are Reserved.</div>
    <div class="footer__social" style="left:318px;top:140px"><i></i><i></i><i></i></div>
  </footer>
</main>

</body>
</html>
```